Website Design for WeselneKarety.pl – Luxury Wedding Car Rental with Chauffeur

We are looking for a talented designer to create a modern, elegant, and fully responsive website for our new brand – WeselnyKarety.pl. We are a premium car rental platform in Poland, offering luxury and exotic vehicles exclusively for weddings. All cars come with a professional chauffeur, ensuring a high-end, stress-free, and stylish experience.
Website Purpose:
The website should present our offering in a luxurious, clear, and inspiring way. It must build trust, highlight the prestige of our brand, and encourage inquiries. Our target audience includes engaged couples, wedding planners, and clients seeking a truly exceptional vehicle for their special day.
Design Requirements:
Style: modern, elegant, minimalist
Color palette: white, black, gold, optionally silver – refined and luxurious
Typography: clean, modern, high-end
Layout: clear, intuitive, with large car images and well-defined sections
Fully responsive (desktop, tablet, mobile)
Bilingual layout (Polish/English) must be considered
Pages to Design:
Homepage
About Us
Fleet Overview
Individual Car Pages
Services (Weddings, Photo Shoots, Film Rentals)
Why Us / Unique Selling Points
Contact
FAQ
Inspiration:
Luxury automotive brands (e.g. Varnell-Dorne, Corwick, Elsby Havard)
High-end wedding websites
Minimalist layouts with large visuals and elegant typography
Additional Notes:
The design should evoke the emotions of a wedding day – elegance, uniqueness, style, and class. Please avoid flashy colors, excessive graphic effects, or overly decorative elements. Subtlety, prestige, and sophistication are key.

```html
<!DOCTYPE html>
<html lang="en">
<head>
<meta charset="utf-8">
<title>WeselnyKarety.pl – Luxury Wedding Cars</title>
<link href="https://fonts.googleapis.com/css2?family=Poppins:wght@800;900&family=Montserrat:wght@400;500;600;700&family=Great+Vibes&display=swap" rel="stylesheet">
<style>
:root{
  --black:#000;
  --gold:#d4af37;
  --gold-dark:#6b5400;
  --ink:#111;
  --muted:#bdbdbd;
  --light:#e6e6e6;
  --white:#fff;
}
*{box-sizing:border-box;margin:0;padding:0}
html,body{width:1200px;height:5381px;overflow:hidden;background:var(--black);font-family:"Montserrat",sans-serif;color:var(--white)}
.page{position:relative;width:1200px;height:5381px}
.abs{position:absolute}
.heading{font-family:"Poppins",sans-serif;font-weight:800;font-size:40px;line-height:1.1}
.center{left:0;width:1200px;text-align:center}

/* nav */
.nav{top:0;left:0;width:1200px;height:84px;background:var(--black)}
.brand{left:46px;top:26px;font-size:22px;font-weight:600;color:var(--gold);display:flex;align-items:center;gap:10px}
.brand-dot{width:14px;height:14px;border-radius:50%;background:var(--gold)}
.menu{left:307px;top:33px;display:flex;gap:26px;font-size:13px;font-weight:600}
.btn-book{left:999px;top:17px;width:153px;height:50px;background:var(--gold);border-radius:6px;color:var(--white);font-weight:700;font-size:18px;display:flex;align-items:center;justify-content:center}

/* hero */
.hero{top:84px;left:0;width:1200px;height:711px;background:linear-gradient(160deg,#3b4236 0%,#5a5d55 45%,#2f302c 100%)}
.hero-title{top:190px;left:0;width:1240px;text-align:center;font-family:"Great Vibes",cursive;font-size:46px}
.hero-sub{top:468px;font-size:30px;font-weight:500}
.btn-gold{left:497px;top:560px;width:245px;height:67px;background:var(--gold);border-bottom:5px solid #a98418;border-radius:6px;display:flex;align-items:center;justify-content:center;font-family:"Poppins",sans-serif;font-weight:800;font-size:24px}

/* about */
.about-title{left:77px;top:856px}
.about-text{left:77px;top:958px;width:560px;font-size:17px;line-height:25px}
.about-text p{margin-bottom:25px}
.collage{left:713px;top:882px;width:403px;height:424px;display:grid;grid-template-columns:1fr 1fr;grid-template-rows:1fr 1fr 1fr;gap:6px}
.ph{background:linear-gradient(135deg,#3d5b63,#9aa6a8)}
.ph.b{background:linear-gradient(135deg,#c9cfd2,#7f8a8f)}
.ph.c{background:linear-gradient(135deg,#2b3c45,#6b7a7e)}

/* fleet */
.fleet{top:1402px;left:0;width:1200px;height:650px;background:var(--gold);color:var(--ink)}
.fleet .heading{top:56px}
.fleet-sub{top:147px;font-size:17px;font-weight:500}
.fleet-card{top:222px;width:345px;height:249px;border:4px solid #8c6e14}
.btn-dark{background:var(--gold-dark);border-bottom:5px solid #3d3000;border-radius:4px;color:var(--white);display:flex;align-items:center;justify-content:center;font-family:"Poppins",sans-serif;font-weight:800;font-size:26px}
.deco{background:linear-gradient(135deg,rgba(140,110,20,.35),rgba(140,110,20,.1))}

/* services */
.services-title{top:2118px}
.services-sub{top:2206px;font-size:17px;font-weight:500}
.svc{top:2285px;width:342px;height:625px;border:3px solid var(--gold);background:linear-gradient(180deg,#1a1a1a,#3a3a3a);padding:5px}
.svc-photo{height:278px}
.svc-name{display:flex;align-items:center;gap:14px;margin:30px 0 0 16px;font-family:"Poppins",sans-serif;font-weight:800;font-size:33px}
.svc-lead{margin:24px 16px 0;font-size:17px;font-weight:700;line-height:24px}
.svc-text{margin:26px 16px 0;font-size:16px;line-height:22px;color:var(--muted)}

/* why */
.why-title{left:77px;top:3058px}
.why-list{left:88px;top:3160px;width:680px;list-style:none;font-size:17px;font-weight:500;line-height:25px}
.why-list li{position:relative;padding-left:20px;margin-bottom:25px}
.why-list li::before{content:"";position:absolute;left:0;top:11px;width:5px;height:5px;border-radius:50%;background:var(--white)}

/* contact */
.contact{top:3626px;left:4px;width:1196px;height:627px;background:var(--gold);color:var(--ink)}
.contact-title{left:73px;top:66px}
.field{left:75px;width:452px;background:var(--white);border:1px solid #ccc;font-size:14px;color:#888;padding:16px 18px}
.info{left:717px;display:flex;align-items:center;gap:26px;font-size:16px;font-weight:500}
.info svg{width:30px;height:30px;fill:#6b5400}

/* faq */
.faq-title{top:4316px}
.faq-item{left:144px;width:916px;height:73px;background:var(--light);color:#333;display:flex;align-items:center;gap:26px;padding-left:22px;font-size:18px;font-weight:500}
.faq-item.open{background:var(--gold);color:var(--white)}
.faq-body{left:144px;top:4700px;width:916px;height:113px;background:var(--light);color:#555;font-size:18px;line-height:28px;padding:26px 38px}
.chev{width:26px;height:26px;stroke:currentColor;fill:none;stroke-width:3}

.footer{top:5282px;left:0;width:1200px;height:99px;background:var(--gold);display:flex;align-items:center;justify-content:center;font-size:20px;font-weight:500}
</style>
</head>
<body>
<div class="page">

<header class="nav abs">
  <div class="brand abs"><span class="brand-dot"></span>WeselnyKarety</div>
  <nav class="menu abs"><span>Home</span><span>About Us</span><span>Fleet Overview</span><span>Services</span><span>Why Us</span><span>Contact</span><span>FAQs</span></nav>
  <div class="btn-book abs">Book Now</div>
</header>

<section class="hero abs" role="img" aria-label="Vintage white wedding car decorated with flowers and ribbons on a tree-lined road"></section>
<h1 class="hero-title abs">Arrive in Elegance. Remember Forever</h1>
<p class="hero-sub abs center">Luxury wedding cars with chauffeur service across Poland</p>
<div class="btn-gold abs">View Our Cars</div>

<h2 class="heading abs about-title">About Us</h2>
<div class="about-text abs">
  <p>WeselnyKarety.pl is Poland’s premier luxury wedding car rental service. We offer an exclusive collection of chauffeur-driven vehicles, carefully selected to bring elegance, class, and timeless beauty to your wedding day.</p>
  <p>We believe your arrival should be as special as the “I do.” That’s why every detail — from polished chrome to the soft hum of the engine — is curated to enhance your once-in-a-lifetime moment.</p>
  <p>With professional chauffeurs, white-glove service, and a fleet of iconic cars, we ensure a smooth, stylish, and stress-free experience — so you can focus on making memories.</p>
</div>
<div class="collage abs">
  <div class="ph" role="img" aria-label="Blue classic car bonnet with a bridal bouquet"></div>
  <div class="ph b" role="img" aria-label="Couple beside a white vintage car"></div>
  <div class="ph c" role="img" aria-label="Bouquet of white and red roses"></div>
  <div class="ph b" role="img" aria-label="Classic blue car on a city street"></div>
  <div class="ph c" role="img" aria-label="Newlyweds inside an open-top car"></div>
  <div class="ph" role="img" aria-label="Decorated wedding car outside townhouses"></div>
</div>

<section class="fleet abs">
  <h2 class="heading abs center">Fleetfoot Overview</h2>
  <p class="fleet-sub abs center">Each vehicle is a statement of style, ready to make your big day unforgettable.</p>
  <div class="deco abs" style="left:1078px;top:158px;width:98px;height:100px" role="img" aria-label="Floral line ornament"></div>
  <div class="deco abs" style="left:20px;top:430px;width:98px;height:100px" role="img" aria-label="Floral line ornament"></div>
  <div class="fleet-card abs ph" style="left:73px" role="img" aria-label="Blue classic car dressed with white and purple bows"></div>
  <div class="fleet-card abs" style="left:428px;background:linear-gradient(135deg,#4d6b2e,#c46a1a 55%,#3a4a25)" role="img" aria-label="Orange sports coupe on a leafy road"></div>
  <div class="fleet-card abs ph b" style="left:781px" role="img" aria-label="Car bonnet with white and purple flowers"></div>
  <div class="btn-dark abs" style="left:474px;top:521px;width:245px;height:69px">View All</div>
</section>

<h2 class="heading abs center services-title">Services</h2>
<p class="services-sub abs center">From fairy-tale weddings to cinematic shoots — our fleet is ready to impress.</p>

<article class="svc abs" style="left:73px">
  <div class="svc-photo" style="background:linear-gradient(135deg,#6b4e3d,#2a2a2a)" role="img" aria-label="Couple holding hands with wedding rings"></div>
  <div class="svc-name"><svg width="52" height="36" viewBox="0 0 52 36" fill="none" stroke="#d4af37" stroke-width="3"><circle cx="18" cy="20" r="13"/><circle cx="34" cy="20" r="13"/></svg>Weddings</div>
  <p class="svc-lead">Make a statement on your special day.</p>
  <p class="svc-text">Arrive in luxury with a chauffeured Varnell-Dorne or Corwick. Whether it’s the bride, groom, or both, we ensure a stress-free, picture-perfect arrival.</p>
</article>
<article class="svc abs" style="left:428px">
  <div class="svc-photo" style="background:linear-gradient(135deg,#8ea26a,#d9d6c8)" role="img" aria-label="Bride and groom walking outdoors"></div>
  <div class="svc-name"><svg width="48" height="36" viewBox="0 0 48 36" fill="#d4af37"><path d="M4 9h10l4-6h12l4 6h10v25H4z"/><circle cx="24" cy="21" r="9" fill="#2a2a2a"/><circle cx="24" cy="21" r="5"/></svg>Photoshoot</div>
  <p class="svc-lead">Create unforgettable moments.</p>
  <p class="svc-text">Our cars are available as props or backdrops for pre-wedding, engagement, or fashion photo sessions. The elegance of each vehicle enhances every frame.</p>
</article>
<article class="svc abs" style="left:781px">
  <div class="svc-photo" style="background:linear-gradient(135deg,#eee,#9a9a9a)" role="img" aria-label="Photo studio with lights and a chair"></div>
  <div class="svc-name"><svg width="42" height="36" viewBox="0 0 42 36" fill="#d4af37"><path d="M2 14h38v20H2z"/><path d="M2 4l36-2 1 8-37 2z"/></svg>Filming</div>
  <p class="svc-lead">Luxury on screen.</p>
  <p class="svc-text">Rent our vehicles for commercials, movies, or music videos. Our fleet adds style, status, and timeless class to any production.</p>
</article>

<div class="deco abs" style="left:74px;top:2944px;width:98px;height:98px" role="img" aria-label="Floral line ornament"></div>
<div class="deco abs" style="left:478px;top:2968px;width:292px;height:26px" role="img" aria-label="Gold scroll divider ornament"></div>

<h2 class="heading abs why-title">Why Choose Us</h2>
<ul class="why-list abs">
  <li>We specialize in wedding transport. Every detail — from chauffeur etiquette to ribbon placement — is tailored for your big day.</li>
  <li>Our fleet includes only top-tier luxury and exotic cars, carefully selected to match the style and elegance of weddings.</li>
  <li>Punctual, discreet, and elegantly dressed, our drivers are trained to provide seamless, stress-free service.</li>
  <li>Our cars arrive immaculate and dressed for the occasion — from satin ribbons to polished wheels.</li>
  <li>We speak both Polish and English fluently, ensuring clear communication with local and international clients.</li>
</ul>
<div class="deco abs" style="left:784px;top:3128px;width:345px;height:312px;border-radius:50%" role="img" aria-label="Gold line illustration of a lily flower"></div>

<section class="contact abs">
  <h2 class="heading abs contact-title">Contact</h2>
  <div class="field abs" style="top:146px;height:57px">Full Name...</div>
  <div class="field abs" style="top:230px;height:56px">Email...</div>
  <div class="field abs" style="top:312px;height:150px">Message...</div>
  <div class="btn-dark abs" style="left:75px;top:489px;width:199px;height:63px;font-size:26px;border-bottom:0">Send</div>
  <div class="info abs" style="top:178px"><svg viewBox="0 0 24 24"><path d="M2 5h20v14H2z M3 6l9 7 9-7" stroke="#d4af37" stroke-width="1"/></svg><span style="text-decoration:underline">hello@weselnykarety.pl</span></div>
  <div class="info abs" style="top:259px"><svg viewBox="0 0 24 24"><path d="M6.6 10.8a15 15 0 0 0 6.6 6.6l2.2-2.2c.3-.3.7-.4 1-.2 1.1.4 2.3.6 3.6.6.6 0 1 .4 1 1V20c0 .6-.4 1-1 1A17 17 0 0 1 3 4c0-.6.4-1 1-1h3.5c.6 0 1 .4 1 1 0 1.3.2 2.5.6 3.6.1.3 0 .7-.2 1z"/></svg><span>+48 512 300 417</span></div>
  <div class="info abs" style="top:345px"><svg viewBox="0 0 24 24"><path d="M12 2a7 7 0 0 0-7 7c0 5.2 7 13 7 13s7-7.8 7-13a7 7 0 0 0-7-7zm0 9.5A2.5 2.5 0 1 1 12 6.5a2.5 2.5 0 0 1 0 5z"/></svg><span>ul. Lipowa 14, 00-512 Warszawa</span></div>
</section>

<h2 class="heading abs center faq-title">Frequently Asked Questions</h2>
<div class="faq-item abs" style="top:4431px"><svg class="chev" viewBox="0 0 24 24"><path d="M5 9l7 7 7-7"/></svg>How far in advance should I book a car?</div>
<div class="faq-item abs" style="top:4529px"><svg class="chev" viewBox="0 0 24 24"><path d="M5 9l7 7 7-7"/></svg>Can I view the car before booking?</div>
<div class="faq-item open abs" style="top:4627px"><svg class="chev" viewBox="0 0 24 24"><path d="M5 15l7-7 7 7"/></svg>Do you only provide cars for weddings?</div>
<div class="faq-body abs">Weddings are our specialty, but we also offer rentals for engagements, pre-wedding shoots, film productions, and luxury events.</div>
<div class="faq-item abs" style="top:4844px"><svg class="chev" viewBox="0 0 24 24"><path d="M5 9l7 7 7-7"/></svg>Can I decorate the car myself?</div>
<div class="faq-item abs" style="top:4943px"><svg class="chev" viewBox="0 0 24 24"><path d="M5 9l7 7 7-7"/></svg>Are your cars chauffeur-driven only?</div>
<div class="faq-item abs" style="top:5041px"><svg class="chev" viewBox="0 0 24 24"><path d="M5 9l7 7 7-7"/></svg>What happens if the car breaks down?</div>
<div class="faq-item abs" style="top:5139px"><svg class="chev" viewBox="0 0 24 24"><path d="M5 9l7 7 7-7"/></svg>How long is the rental period?</div>

<footer class="footer abs">Copyright © 2025 WeselnyKarety.pl</footer>
</div>
</body>
</html>
```